Flyer for Programming Classes for Kids

We are small school in Tokyo, Japan teaching computer programming to kids in English.
We need a flyer to promote our classes and provide basic information about our company.
See Flyer_Notes.doc for more company info, class info, and flyer requirements.
Basic Info:
One page flyer. Two-sided, front and back.
We would like a flyer that introduces the company. -and-
Highlights the classes we offer
Target Market: 6-12 year old kids and their parents. Audience is English speaking families in Japan.
Look And Feel: Bold, Playful, Modern, Conservative
Paper Size: B4
What is B4? https://www.quorvanta.com/products/resources/paper-sizes-and-formats-explained.php
Target Market(s)
Tokyo, but English speakers
Industry/Entity Type
Education
Colors
Designer to choose colors to be used in the design.
Look and feel
Each slider illustrates characteristics of the customer's brand and the style your logo design should communicate.

```html
<!DOCTYPE html>
<html lang="en">
<head>
<meta charset="utf-8">
<title>Byte Garden – Coding Classes for Kids</title>
<link href="https://fonts.googleapis.com/css2?family=Montserrat:wght@700;800&family=Josefin+Sans:wght@300;400&display=swap" rel="stylesheet">
<style>
  :root {
    --page: #ffffff;
    --teal: #4cc4a2;
    --mid: #4f9ba8;
    --indigo: #4b5fb2;
    --white: #ffffff;
    --badge-bg: #ffffff;
    --badge-mark: #d9b45a;
  }
  * { margin: 0; padding: 0; box-sizing: border-box; }
  html, body { width: 880px; height: 1200px; overflow: hidden; background: var(--page); }
  .flyer {
    position: absolute; left: 30px; top: 29px; width: 817px; height: 1145px;
    background: linear-gradient(180deg, var(--teal) 0%, var(--mid) 48%, var(--indigo) 100%);
    overflow: hidden; color: var(--white);
  }
  .classroom-photo {
    position: absolute; left: 0; top: 500px; width: 100%; height: 645px;
    background: radial-gradient(ellipse at 50% 45%, rgba(50,80,130,0.28), rgba(50,80,130,0) 70%);
  }
  .headline-frame {
    position: absolute; left: 150px; top: 190px; width: 517px; height: 220px;
    border: 4px solid var(--white); border-radius: 28px;
  }
  .headline {
    position: absolute; left: 0; width: 100%; top: 240px; text-align: center;
    font-family: 'Montserrat', sans-serif; font-weight: 800; font-size: 46px; line-height: 60px;
    letter-spacing: 0.5px;
  }
  .ages {
    position: absolute; left: 212px; top: 508px;
    font-family: 'Montserrat', sans-serif; font-weight: 800; font-size: 72px; line-height: 82px;
  }
  .details {
    position: absolute; left: 479px; top: 488px;
    font-family: 'Josefin Sans', sans-serif; font-weight: 300; font-size: 32px;
  }
  .details p { line-height: 53px; }
  .details .enroll { line-height: 32px; margin-top: 6px; }
  .badge {
    position: absolute; top: 736px; width: 186px; height: 117px; background: var(--badge-bg);
    display: flex; align-items: center; justify-content: center;
  }
  .badge--award { left: 211px; }
  .badge--listing { left: 422px; }
  .badge-mark { width: 70px; height: 70px; border-radius: 50%; background: var(--badge-mark); }
  .brand {
    position: absolute; left: 0; width: 100%; top: 874px; text-align: center;
    font-family: 'Montserrat', sans-serif; font-weight: 700; font-size: 52px; line-height: 62px;
  }
  .tagline {
    position: absolute; left: 0; width: 100%; top: 950px; text-align: center;
    font-family: 'Josefin Sans', sans-serif; font-weight: 400; font-size: 17px; letter-spacing: 0.5px;
  }
  .divider {
    position: absolute; left: 212px; top: 1003px; width: 396px; height: 3px; background: var(--white);
  }
  .contact {
    position: absolute; top: 1029px; font-style: normal;
    font-family: 'Josefin Sans', sans-serif; font-weight: 300; font-size: 12.5px; line-height: 15px;
  }
  .contact--address { left: 212px; }
  .contact--reach { left: 467px; }
</style>
</head>
<body>
<main class="flyer">
  <div class="classroom-photo" role="img" aria-label="Faded photo of a laptop showing a block-based coding program in a classroom"></div>

  <div class="headline-frame" aria-hidden="true"></div>
  <h1 class="headline">CODING CLASSES<br>FOR KIDS!</h1>

  <p class="ages">AGES<br>6 - 12</p>

  <div class="details">
    <p>Taught in</p>
    <p>English</p>
    <p class="enroll">Enroll for<br>Summer<br>Camps<br>Now!</p>
  </div>

  <div class="badge badge--award"><span class="badge-mark"></span></div>
  <div class="badge badge--listing"><span class="badge-mark"></span></div>

  <p class="brand">Byte Garden</p>
  <p class="tagline">Small Steps, Big Ideas</p>

  <div class="divider"></div>

  <address class="contact contact--address">
    Close to Hanamura &amp; Kitano Stations<br>
    3-14-8 Maple Court Hanamura 2F<br>
    Kitano-ku Hanamura, Tokyo 150-0042
  </address>
  <address class="contact contact--reach">
    info@bytegarden.jp<br>
    070-5381-2270 (Japanese)<br>
    070-5381-2294 (English)<br>
    http://bytegarden.jp
  </address>
</main>
</body>
</html>
```